Website Design - Photo Shop Design - Functional Cash Register Layout for POS System

Design a webpage for Point of Sale site. A cash register page.

Page must have a good look. I have attached a file of a possible layout example - but need a much nicer design. I have also attached the site logo. which i will upload without background tomorrow hopefully.

Looking for a nice Fresh look , not dark and dingy.

Target Market(s)

Business

Industry/Entity Type

Business Software

Number of Pages Required

1 page

Colors
f59195
f04a50
ec1f27
fbd4d5
ffffff
f8f3f8
fdf0f6
feeeee
ecf5f6

Requirements
Must have
• Cash register layout for POS software site. Nice layout ,
Nice to have
• Try putting he register part on the left side as well as the right - invert the designs have them different to the layout example shown too.
Should not have
• Not to dark

```html
<!DOCTYPE html>
<html lang="en">
<head>
<meta charset="utf-8">
<title>TillNimbus – Enter Sale</title>
<link rel="stylesheet" href="https://fonts.googleapis.com/css2?family=Open+Sans:wght@400;600;700&family=Roboto:wght@400;500;700&display=swap">
<style>
:root{
  --red:#ec1f27;
  --red-dark:#d81a22;
  --pink-soft:#fbd4d5;
  --page:#feeeee;
  --white:#ffffff;
  --tile:#ecf5f6;
  --bar:#f8f3f8;
  --line:#dcdcdc;
  --ink:#333333;
  --muted:#555555;
}
*{box-sizing:border-box;margin:0;padding:0}
html,body{width:1200px;height:779px;overflow:hidden}
body{position:relative;background:var(--page);font-family:"Open Sans",sans-serif;color:var(--ink)}
.abs{position:absolute}

/* header */
.topbar{left:0;top:0;width:1200px;height:75px;background:var(--white);box-shadow:0 1px 3px rgba(0,0,0,.15);z-index:2}
.brand{left:38px;top:18px;display:flex;align-items:center;gap:8px}
.brand-dot{width:22px;height:22px;border-radius:50%;background:var(--red)}
.brand-name{font-size:28px;font-weight:700;color:var(--ink);letter-spacing:-.5px;line-height:1}
.brand-sub{left:200px;top:52px;font-size:7px;color:var(--muted)}
.pill{top:20px;height:36px;border-radius:18px;font-family:Roboto,sans-serif;font-weight:500;font-size:15px;display:flex;align-items:center;justify-content:center}
.pill-shop{left:811px;width:98px;background:var(--red);color:var(--white)}
.pill-register{left:919px;width:150px;border:1px solid #bbb;color:var(--ink)}
.menu-icon{left:1086px;top:31px}

/* sidebar */
.sidebar{left:0;top:75px;width:256px;height:704px;background:var(--red)}
.nav-item{left:0;width:256px;height:48px;display:flex;align-items:center;padding-left:50px;color:var(--white);font-family:Roboto,sans-serif;font-weight:500;font-size:13px;gap:0}
.nav-item svg{position:absolute;left:50px}
.nav-item span{margin-left:37px}
.nav-item.active{background:var(--pink-soft);color:var(--ink)}
.nav-chevron{position:absolute;right:30px}
.store-badge{left:49px;top:444px;width:136px;height:49px;border-radius:7px;background:#000;border:2px solid var(--white)}
.social{top:710px;width:36px;height:36px;border-radius:50%;border:1.5px solid var(--white)}

/* product panel */
.panel{background:var(--white);border:1px solid #e4dada}
.products{left:279px;top:117px;width:560px;height:557px}
.search{left:293px;top:138px;width:533px;height:45px;border:1px solid #c8c8c8;border-radius:23px;display:flex;align-items:center;padding-left:30px;font-size:15px;color:var(--muted)}
.search-btn{left:764px;top:138px;width:62px;height:45px;border-radius:23px;background:var(--red);display:flex;align-items:center;justify-content:center}
.tile{width:123px;height:128px;background:var(--white);border:1px solid #e0e0e0;box-shadow:0 1px 2px rgba(0,0,0,.08)}
.tile-face{position:absolute;left:4px;top:4px;right:4px;height:91px;background:var(--tile);display:flex;align-items:center;justify-content:center;font-weight:700;font-size:44px;color:#2a2a2a}
.tile-name{position:absolute;left:0;right:0;top:103px;text-align:center;font-size:14px;color:var(--ink)}
.page-btn{top:579px;height:26px;width:26px;border:1px solid #ddd;background:#f7f7f7;font-size:12px;display:flex;align-items:center;justify-content:center;color:var(--ink);font-family:Roboto,sans-serif}
.page-btn.wide{width:51px}
.page-btn.current{background:var(--red);color:var(--white);border-color:var(--red)}
.catbar{left:279px;top:636px;width:560px;height:38px;background:var(--bar);border-top:1px solid #e2dde2;display:flex}
.cat{height:100%;display:flex;align-items:center;justify-content:center;font-family:Roboto,sans-serif;font-weight:500;font-size:14px;color:var(--ink);border-right:1px solid #e2dde2}
.cat.left-al{justify-content:flex-start;padding-left:18px}

/* cart */
.cart{left:861px;top:117px;width:287px;height:557px}
.cart-head{left:862px;top:118px;width:285px;height:47px;background:var(--bar);border-bottom:1px solid #e2dde2}
.cart-customer{left:911px;top:127px;font-size:14px;line-height:15px}
.cart-divider{left:1040px;top:118px;width:1px;height:47px;background:#e2dde2}
.cart-txn{left:1046px;top:127px;width:90px;text-align:right;font-size:14px;line-height:15px}
.notes{left:878px;top:543px;font-size:13px;font-weight:600;color:var(--ink)}
.totals{left:862px;width:285px;text-align:center;font-size:11px;color:var(--muted)}
.cart-rule{left:869px;top:617px;width:273px;height:2px;background:#e2e2e2}
.cart-btn{top:632px;height:30px;display:flex;align-items:center;justify-content:center;font-family:Roboto,sans-serif;font-size:13px}
.btn-add{left:872px;width:29px;background:#dfe7ea;font-size:16px}
.btn-save{left:905px;width:134px;background:#dfe7ea;color:var(--ink)}
.btn-pay{left:1043px;width:96px;background:var(--red);color:var(--white);font-size:15px;font-weight:500;justify-content:space-between;padding:0 9px}

.footer{left:256px;width:944px;top:722px;text-align:center;font-size:13px;color:var(--muted)}
.chat{left:1094px;top:732px;width:46px;height:46px;border-radius:50%;background:var(--red);box-shadow:0 2px 5px rgba(0,0,0,.25);display:flex;align-items:center;justify-content:center}
.corner-code{left:1159px;top:745px;font-size:15px;font-family:Roboto,sans-serif;color:var(--ink)}
</style>
</head>
<body>

<header class="abs topbar">
  <div class="abs brand"><div class="brand-dot"></div><div class="brand-name">TillNimbus</div></div>
  <div class="abs brand-sub">powered by NIMBA</div>
  <div class="abs pill pill-shop">MY SHOP</div>
  <div class="abs pill pill-register">CASH REGISTER 1</div>
  <svg class="abs menu-icon" width="16" height="14" viewBox="0 0 16 14"><rect y="1" width="16" height="2.4" fill="#555"/><rect y="6" width="16" height="2.4" fill="#555"/><rect y="11" width="16" height="2.4" fill="#555"/></svg>
</header>

<nav class="abs sidebar">
  <div class="abs nav-item active" style="top:43px">
    <svg width="20" height="18" viewBox="0 0 20 18"><path d="M10 1 1 9h3v8h4.5v-5h3v5H16V9h3z" fill="#ec1f27"/></svg><span>ENTER SALE</span>
  </div>
  <div class="abs nav-item" style="top:108px">
    <svg width="20" height="20" viewBox="0 0 20 20"><path d="M8 1h4v7h3l-5 6-5-6h3z" fill="#fff"/><rect x="1" y="14" width="18" height="5" rx="1" fill="#fff"/></svg><span>PARKED/LAYBY ORDERS</span>
  </div>
  <div class="abs nav-item" style="top:173px">
    <svg width="22" height="20" viewBox="0 0 22 20"><rect x="1.5" y="3.5" width="15" height="15" rx="2" fill="none" stroke="#fff" stroke-width="2.2"/><path d="M5 10l4 4 11-11" fill="none" stroke="#fff" stroke-width="3"/></svg><span>COMPLETED SALES</span>
  </div>
  <div class="abs nav-item" style="top:238px">
    <svg width="22" height="22" viewBox="0 0 22 22"><rect x="1" y="3" width="20" height="18" rx="1" fill="none" stroke="#fff" stroke-width="2"/><rect x="1" y="3" width="20" height="5" fill="#fff"/><rect x="5" y="0" width="2.5" height="5" fill="#fff"/><rect x="14.5" y="0" width="2.5" height="5" fill="#fff"/><path d="M4 12h14M4 16h14M8 9v11M14 9v11" stroke="#fff" stroke-width="1.3"/></svg><span>APPOINTMENTS</span>
  </div>
  <div class="abs nav-item" style="top:303px">
    <svg width="20" height="20" viewBox="0 0 20 20"><circle cx="10" cy="10" r="9.5" fill="#fff"/><rect x="8.5" y="8" width="3" height="8" fill="#ec1f27"/><circle cx="10" cy="5" r="1.7" fill="#ec1f27"/></svg><span>BACK OFFICE</span>
    <svg class="nav-chevron" style="left:auto;right:30px" width="7" height="11" viewBox="0 0 7 11"><path d="M1 1l4.5 4.5L1 10" fill="none" stroke="#fff" stroke-width="1.6"/></svg>
  </div>
  <div class="abs store-badge" style="top:369px"></div>
  <div class="abs nav-item" style="top:433px">
    <svg width="20" height="20" viewBox="0 0 20 20"><path d="M3 9a7 7 0 0 1 12.5-4" fill="none" stroke="#fff" stroke-width="2.6"/><path d="M17 1v6h-6z" fill="#fff"/><path d="M17 11a7 7 0 0 1-12.5 4" fill="none" stroke="#fff" stroke-width="2.6"/><path d="M3 19v-6h6z" fill="#fff"/></svg><span>REFRESH DATA</span>
  </div>
  <div class="abs social" style="left:23px;top:635px"></div>
  <div class="abs social" style="left:66px;top:635px"></div>
  <div class="abs social" style="left:110px;top:635px"></div>
  <div class="abs social" style="left:153px;top:635px"></div>
  <div class="abs social" style="left:196px;top:635px"></div>
</nav>

<section class="abs panel products"></section>
<div class="abs search">Search Product by name or Sku</div>
<div class="abs search-btn"><svg width="22" height="22" viewBox="0 0 22 22"><circle cx="9" cy="9" r="6.5" fill="none" stroke="#fff" stroke-width="3"/><path d="M14 14l6 6" stroke="#fff" stroke-width="3.4" stroke-linecap="round"/></svg></div>

<div class="abs tile" style="left:294px;top:220px"><div class="tile-face">DP</div><div class="tile-name">Demo Product</div></div>
<div class="abs tile" style="left:430px;top:220px"><div class="tile-face">EL</div><div class="tile-name">Entry Level com..</div></div>
<div class="abs tile" style="left:567px;top:220px"><div class="tile-face">GC</div><div class="tile-name">Gift card</div></div>
<div class="abs tile" style="left:704px;top:220px"><div class="tile-face">P5</div><div class="tile-name">Product 5</div></div>
<div class="abs tile" style="left:294px;top:375px"><div class="tile-face">T2</div><div class="tile-name">Test 2</div></div>
<div class="abs tile" style="left:430px;top:375px"><div class="tile-face">T3</div><div class="tile-name">Test 3</div></div>
<div class="abs tile" style="left:567px;top:375px"><div class="tile-face">FA</div><div class="tile-name">Fasdfadfasdf</div></div>
<div class="abs tile" style="left:704px;top:375px"><div class="tile-face">T6</div><div class="tile-name">Test 6</div></div>

<div class="abs page-btn wide" style="left:366px">Prev</div>
<div class="abs page-btn current" style="left:427px">1</div>
<div class="abs page-btn" style="left:461px">2</div>
<div class="abs page-btn" style="left:495px">3</div>
<div class="abs page-btn" style="left:529px">4</div>
<div class="abs page-btn" style="left:563px">5</div>
<div class="abs page-btn" style="left:597px">6</div>
<div class="abs page-btn" style="left:631px">...</div>
<div class="abs page-btn" style="left:666px">22</div>
<div class="abs page-btn wide" style="left:701px">Next</div>

<div class="abs catbar">
  <div class="cat" style="width:45px"><svg width="8" height="14" viewBox="0 0 8 14"><path d="M7 1 1 7l6 6" fill="none" stroke="#888" stroke-width="1.5"/></svg></div>
  <div class="cat" style="width:99px">LIST ALL</div>
  <div class="cat" style="width:80px">DEALS</div>
  <div class="cat left-al" style="width:291px">UNCATEGORIZED</div>
  <div class="cat" style="width:45px;border-right:0"><svg width="8" height="14" viewBox="0 0 8 14"><path d="M1 1l6 6-6 6" fill="none" stroke="#888" stroke-width="1.5"/></svg></div>
</div>

<aside class="abs panel cart"></aside>
<div class="abs cart-head"></div>
<svg class="abs" style="left:875px;top:128px" width="22" height="24" viewBox="0 0 22 24"><circle cx="11" cy="7" r="6" fill="#ec1f27"/><path d="M0 24c0-7 5-10 11-10s11 3 11 10z" fill="#ec1f27"/></svg>
<div class="abs cart-customer">Select<br>Customer</div>
<div class="abs cart-divider"></div>
<div class="abs cart-txn">Transaction#<br>00016</div>
<div class="abs notes">ADD NOTES</div>
<div class="abs totals" style="top:570px">Subtotal : $0.00 | Tax : $0.00 | Disc : $0.00</div>
<div class="abs totals" style="top:588px">Total : $0.00 | Paid : $0.00</div>
<div class="abs cart-rule"></div>
<div class="abs cart-btn btn-add">+</div>
<div class="abs cart-btn btn-save">SAVE &amp; PARK/LAYBY</div>
<div class="abs cart-btn btn-pay"><span>PAY</span><span>$0.00</span></div>

<footer class="abs footer">Copyright 2016, TillNimbus, Inc. All rights reserved | Terms &amp; Conditions</footer>
<div class="abs chat"><svg width="26" height="22" viewBox="0 0 26 22"><ellipse cx="13" cy="9.5" rx="12" ry="8.5" fill="#fff"/><path d="M5 15l-2 6 7-4z" fill="#fff"/><circle cx="8" cy="9.5" r="1.8" fill="#ec1f27"/><circle cx="13" cy="9.5" r="1.8" fill="#ec1f27"/><circle cx="18" cy="9.5" r="1.8" fill="#ec1f27"/></svg></div>
<div class="abs corner-code">C17</div>

</body>
</html>
```